Software Company Banner Ad

We need a banner ad in two sizes. 728x90 and 300x250.
They should have strong similarity to the following ads:
http://www.vexlo.net/search/results?brand[0]=quorp&ad=4821396
http://www.vexlo.net/search/results?brand[0]=dravensoft&ad=4830517
Idea will be very similar. We want the same grey color, white text, and a realistic owl that blinks. The owl should have dramatic, bright, yellow eyes. The text will animate "from the top" as in the example. Though the logo animation will be different, all text and non-logo animation should match the animation in the example advertisements. The text will rotate between the following four sentences and images.
Looking for a provider of procurement cloud apps?
[Images - attached below]
The experts really liked our KTV booth.
Get great results with every procurement. [Learn more]
There are three vector files attached below. Feel free to change the colors as necessary to match the color scheme of the ad. We need one 2013 and one 2014 award in the ad.
The awards could appear simultaneously, could swap with each other or could appear in succession. Animation is acceptable.
There is an additional vector file with the company logo. The company logo should go where the Quorp logo is in horizontal ad. The company logo should go where the Dravensoft logo is in the block ad. The example ad has two logos. We will only need one logo on our ads. The logo should be changed to the color of the text used for the ad (white).
The owls eyes should slowly blink two times (as in the example).
The owl eyes should immediately grab someone's attention and all colors should compliment these eyes.
The [Learn more] button should have animation. The button should match the color of the owl's eyes. There should be a line/gleam/glare of light that travels across the button. The button should be embossed with the subtle animation occurring each time it appears.
Ads should be done with flash. We will need the source files and the names of any fonts used at the end of the project.
Thank you and please do not hesitate to contact with any questions.
Reason: We have contacted several photographers to see if the alternative owl images are available on Pixvane, Framelodge or similar. The duration extension is to accommodate this.
Target Market(s)
Target customers are procurement department employees of large companies.
Industry/Entity Type
It Company

```html
<!DOCTYPE html>
<html lang="en">
<head>
<meta charset="utf-8">
<title>Procurement Banner – Sample 1</title>
<link href="https://fonts.googleapis.com/css2?family=PT+Sans:wght@400;700&display=swap" rel="stylesheet">
<style>
  :root {
    --ink: #333333;
    --banner-grey: #58585a;
    --banner-text: #ffffff;
    --photo-deep: #6e4a2a;
    --photo-mid: #9c7046;
    --photo-light: #b58a5e;
    --badge-fill: #f2f2f2;
    --eye-yellow: #f3c316;
    --eye-amber: #eaa80c;
    --button-text: #2a2200;
    --bg-center: #ffffff;
    --bg-edge: #e2e2e2;
  }
  * { margin: 0; padding: 0; box-sizing: border-box; }
  html, body { width: 1200px; height: 1000px; overflow: hidden; }
  body {
    position: relative;
    font-family: "PT Sans", "Myriad Pro", Arial, sans-serif;
    color: var(--ink);
    background: radial-gradient(ellipse 60% 55% at 50% 45%, var(--bg-center) 0%, #f6f6f6 50%, var(--bg-edge) 100%);
  }
  .sheet-title {
    position: absolute; top: 44px; left: 0; width: 1244px;
    text-align: center; font-size: 40px; font-weight: 700; color: var(--ink);
  }
  .slide-label {
    position: absolute; width: 240px; text-align: right; color: var(--ink);
  }
  .slide-label .name { display: block; font-size: 31px; line-height: 32px; }
  .slide-label .note { display: block; font-size: 15.5px; line-height: 18px; }

  .banner {
    position: absolute; width: 728px; height: 90px;
    background: var(--banner-grey); color: var(--banner-text); overflow: hidden;
  }
  .banner .brand {
    position: absolute; left: 8px; top: 9px;
    font-size: 17px; font-weight: 700; letter-spacing: 1.5px; line-height: 18px;
    color: var(--banner-text);
  }
  .banner .message {
    position: absolute; font-size: 17.5px; line-height: 24px; color: var(--banner-text);
    white-space: nowrap;
  }
  .banner .owl-photo {
    position: absolute; right: 0; top: 0; width: 341px; height: 90px;
    background: linear-gradient(90deg, var(--photo-deep) 0%, var(--photo-mid) 30%, var(--photo-light) 50%, var(--photo-mid) 70%, var(--photo-deep) 100%);
  }
  .award-badge {
    position: absolute; left: 18px; top: 15px; width: 60px; height: 60px;
    background: var(--badge-fill);
  }
  .award-source {
    position: absolute; left: 106px; top: 19px; font-size: 18px; line-height: 24px;
    white-space: nowrap;
  }
  .award-title {
    position: absolute; left: 106px; top: 45px; font-size: 24px; font-weight: 700; line-height: 30px; letter-spacing: 0.3px;
    white-space: nowrap;
  }
  .learn-more {
    position: absolute; left: 289px; top: 53px; width: 81px; height: 24px;
    border-radius: 3px;
    background: linear-gradient(180deg, #f8d43a 0%, var(--eye-yellow) 50%, var(--eye-amber) 100%);
    box-shadow: inset 0 1px 0 rgba(255,255,255,0.5), 0 1px 1px rgba(0,0,0,0.3);
    font-family: Arial, Helvetica, sans-serif; font-size: 12px; line-height: 24px;
    text-align: center; color: var(--button-text);
  }
</style>
</head>
<body>
  <h1 class="sheet-title">Sample 1</h1>

  <div class="slide-label" style="left:12px; top:174px;"><span class="name">Slide 1</span><span class="note">with tagline</span></div>
  <div class="banner" style="left:278px; top:151px;">
    <span class="brand">ORVEL</span>
    <p class="message" style="left:85px; top:23px;">Looking for a provider of procurement<br>cloud apps?</p>
    <div class="owl-photo" role="img" aria-label="Close-up photo of an owl with bright yellow eyes"></div>
  </div>

  <div class="slide-label" style="left:12px; top:370px;"><span class="name">Slide 2</span><span class="note">with tagline</span></div>
  <div class="banner" style="left:277px; top:351px;">
    <span class="brand">ORVEL</span>
    <p class="message" style="left:83px; top:33px;">The experts really liked our KTV booth</p>
    <div class="owl-photo" role="img" aria-label="Close-up photo of an owl with bright yellow eyes"></div>
  </div>

  <div class="slide-label" style="left:13px; top:566px;"><span class="name">Slide 3</span><span class="note">with award 2013</span></div>
  <div class="banner" style="left:277px; top:549px;">
    <div class="award-badge" role="img" aria-label="Award badge"></div>
    <span class="award-source">Sourcing Review</span>
    <span class="award-title">BEST OF SHOW 2013</span>
    <div class="owl-photo" role="img" aria-label="Close-up photo of an owl with bright yellow eyes"></div>
  </div>

  <div class="slide-label" style="left:13px; top:760px;"><span class="name">Slide 4</span><span class="note">with Learn more button</span></div>
  <div class="banner" style="left:278px; top:741px;">
    <span class="brand">ORVEL</span>
    <p class="message" style="left:99px; top:22px;">Get great results with every<br>procurement.</p>
    <span class="learn-more">Learn More</span>
    <div class="owl-photo" role="img" aria-label="Close-up photo of an owl with bright yellow eyes"></div>
  </div>
</body>
</html>
```